Plakat-Design Workshop gegen Prüfungsangst
Zielgruppe
Prüfungsangst überwinden mittels Workshops: 'Selbsthypnose erlernen'
Zielgruppe Studenten
Schweißausbrüche, Blackout, und Resignation.
Viele kennen diese unangenehmen Momente, wenn eine Prüfung begonnen hat und die Aufgabenstellungen scheinbar unlösbar sind.
Dann ist Entspannung nahezu unmöglich. Das Stresshormon Cortisol wurde bereits ausgeschüttet. Es beeinträchtigt die Erinnerung an das Gelernte.
Die mentale Vorbereitung sollte schon viel eher ansetzen, wenn es noch nicht zu spät ist. Wenn der Körper noch nicht verkrampft ist.
Selbsthypnose vor Prüfungen ist hier eine tolle Möglichkeit.
Mit Hilfe einer geführten Selbsthypnoseanleitung ist es Dir möglich Dein Unterbewusstsein so zu programmieren, dass diese Übererregungszustände vor Prüfungssituationen deutlich reduziert werden.
Aufgabenstellung
DINA 4 Plakat, 'Prüfungsangst?' mit einem Freifeld, wo man Ort, Datum und Zeit der Veranstaltung 'Selbsthypnose erlernen'
(Selbstsicher in die Prüfung) eindrucken kann.
darunter:
Anmeldung: Tel: 01563 8274015
Dipl. Sportl. Henrik Malow Mentaltraining
weitere Infos auch über Einzelsitzungen: www.malow-trance.de

```html
<!DOCTYPE html>
<html lang="de">
<head>
<meta charset="utf-8">
<title>Prüfungsangst? – Workshop Selbsthypnose</title>
<link rel="stylesheet" href="https://fonts.googleapis.com/css2?family=Catamaran:wght@400;600;700&display=swap">
<style>
  :root {
    --red: #e0312a;
    --black: #0a0a0a;
    --ink: #111111;
    --white: #ffffff;
    --paper: #fdfdfd;
  }
  * { margin: 0; padding: 0; box-sizing: border-box; }
  html, body {
    width: 881px; height: 1200px; overflow: hidden;
    background: var(--white);
    font-family: "Catamaran", Arial, sans-serif;
    color: var(--ink);
  }
  .poster {
    position: absolute; left: 51px; top: 51px;
    width: 772px; height: 1092px;
    background: var(--paper);
    box-shadow: 0 4px 14px rgba(0,0,0,0.35);
    overflow: hidden;
  }
  .hero-photo {
    position: absolute; left: 0; top: 0; width: 433px; height: 209px;
    background: linear-gradient(100deg, #8a2b36 0%, #a33a40 30%, #c97d55 60%, #d9955f 100%);
  }
  .brand-panel {
    position: absolute; left: 433px; top: 0; right: 0; height: 209px;
    background: var(--black);
    color: var(--white);
    text-align: center;
  }
  .brand-name {
    position: absolute; left: 0; right: 0; top: 124px;
    font-size: 32px; font-weight: 700; letter-spacing: 2px; line-height: 1;
  }
  .rule {
    position: absolute; left: 0; right: 0; top: 214px; height: 6px;
    background: var(--red);
  }
  .headline {
    position: absolute; left: 25px; top: 281px;
    font-size: 110px; font-weight: 600; line-height: 1;
    letter-spacing: -1.5px; color: var(--red);
    white-space: nowrap;
  }
  .subhead {
    position: absolute; left: 27px; top: 396px;
    font-size: 36px; font-weight: 700; line-height: 1;
    white-space: nowrap;
  }
  .intro {
    position: absolute; left: 27px; top: 443px; width: 740px;
    font-size: 27.5px; font-weight: 400; line-height: 35px;
  }
  .claim {
    position: absolute; left: 27px; top: 652px;
    font-size: 63px; font-weight: 600; line-height: 1;
    letter-spacing: -0.5px; color: var(--red);
    white-space: nowrap;
  }
  .trainer-photo {
    position: absolute; left: 29px; top: 741px; width: 217px; height: 306px;
    background: linear-gradient(160deg, #8d8d8d 0%, #b7bcc4 45%, #9fb6d6 75%, #6f7d8f 100%);
  }
  .seal {
    position: absolute; left: 196px; top: 945px; width: 140px; height: 140px;
  }
  .event-fields {
    position: absolute; left: 358px; top: 712px; width: 390px;
  }
  .field {
    display: flex; align-items: flex-end;
    height: 61px;
    font-size: 42px; line-height: 1;
  }
  .field-line {
    flex: 1; margin-left: 3px; margin-bottom: 7px;
    border-bottom: 2px solid var(--ink);
  }
  .registration {
    position: absolute; left: 358px; top: 930px; width: 410px;
    font-size: 23px; line-height: 25px;
    white-space: nowrap;
  }
  .registration strong { font-weight: 700; }
  .footer-band {
    position: absolute; left: 0; right: 0; bottom: 0; height: 32px;
    background: var(--red);
  }
</style>
</head>
<body>
  <main class="poster">
    <div class="hero-photo" role="img" aria-label="Foto: gestresster Student stützt den Kopf in die Hand"></div>
    <header class="brand-panel">
      <div class="brand-name">MALOW-TRANCE</div>
    </header>
    <div class="rule"></div>

    <h1 class="headline">Prüfungsangst?</h1>
    <h2 class="subhead">Schweißausbrüche, Blackout &amp; Resignation?</h2>
    <p class="intro">Im Workshop "Selbsthypnose" lernst Du Strategien, solche Übererregungszustände vor Prüfungen deutlich zu reduzieren.</p>

    <h2 class="claim">Selbstsicher in die Prüfung!</h2>

    <div class="trainer-photo" role="img" aria-label="Porträtfoto des Mentaltrainers vor einer Betonwand"></div>
    <svg class="seal" viewBox="0 0 140 140" aria-hidden="true">
      <circle cx="70" cy="70" r="70" fill="#ffffff"/>
      <circle cx="70" cy="70" r="62" fill="#e3ecef" stroke="#3a8c9a" stroke-width="2"/>
      <circle cx="70" cy="70" r="40" fill="#cfdde2"/>
      <circle cx="70" cy="70" r="30" fill="#137f8d"/>
    </svg>

    <section class="event-fields">
      <div class="field">Ort:<span class="field-line"></span></div>
      <div class="field">Datum:<span class="field-line"></span></div>
      <div class="field">Zeit:<span class="field-line"></span></div>
    </section>

    <section class="registration">
      <strong>Anmeldung:</strong><br>
      Tel: 01563 8274015<br>
      Dipl. Sportl. Henrik Malow Mentaltraining<br>
      weitere Infos auch über Einzelsitzungen:<br>
      <strong>www.malow-trance.de</strong>
    </section>

    <div class="footer-band"></div>
  </main>
</body>
</html>
```